Business Card Design

We need a new business card design for our corporate executives. We are a very niche business working in the Aviation Night Vision Goggle Industry. I am looking for a design that has a "corporate" look and feel. I would like to see designs that incorporate a clean look with possibly raised letters, foil, or any other current design elements available. I am open to design elements/information being placed on the back of the business card but also want to be able to write on the back of the card to take notes. Back-side design is not mandatory.

Company Overview
At Copperline Aeroworks, the most experienced team implements the highest quality night vision equipment, maintenance, and training procedures available to offer a comprehensive Night Vision Solution that enhances the safety and operational capabilities of all aviation organizations.

Our team is dedicated to client success and satisfaction throughout the entire night vision goggle solution lifecycle. Our solutions are designed to meet customer operational needs so that organizations can efficiently and effectively realize their goals – while increasing performance, reducing costs and enhancing safety.

Industry/Entity Type

Training

Contact Information for Business Card

Grant L. Whitcombe, President, Copperline Aeroworks, Inc., copperlineaeroworks.example, grant.whitcombe@copperlineaeroworks.example, (555) 214-7390, (company toll free #) (888) 555-0147

```html
<!DOCTYPE html>
<html lang="en">
<head>
<meta charset="utf-8">
<title>Copperline Aeroworks — Business Card</title>
<link rel="stylesheet" href="https://fonts.googleapis.com/css2?family=Roboto:wght@300;400;700&display=swap">
<style>
  :root {
    --green-deep: #3a9445;
    --green-light: #8cc63f;
    --ink: #2b2b2d;
    --ink-soft: #4a4a4a;
    --paper: #ffffff;
    --backdrop: #e9e7e2;
  }
  * { box-sizing: border-box; margin: 0; padding: 0; }
  html, body {
    width: 1200px; height: 800px; overflow: hidden;
    background: var(--backdrop);
    font-family: "Roboto", Arial, sans-serif;
  }
  .sheet {
    width: 1200px; height: 800px;
    display: flex; align-items: center; justify-content: center; gap: 40px;
  }
  .card {
    position: relative;
    width: 540px; height: 309px;
    background: var(--paper);
    overflow: hidden;
    box-shadow: 0 6px 18px rgba(0,0,0,.18);
  }
  .card-art { position: absolute; inset: 0; width: 100%; height: 100%; }
  .brand {
    position: absolute;
    display: flex; align-items: center; gap: 12px;
    white-space: nowrap;
  }
  .brand-dot {
    width: 34px; height: 34px; border-radius: 50%;
    background: var(--green-deep);
    flex: none;
  }
  .brand-name {
    font-weight: 700; color: var(--ink);
    font-size: 24px; letter-spacing: .5px; text-transform: uppercase;
    line-height: 1;
  }
  .card-front .brand { left: 50%; top: 48%; transform: translate(-50%, -50%); }
  .card-back .brand { left: 40px; top: 58px; }
  .card-back .brand-name { font-size: 22px; }
  .contact {
    position: absolute; right: 22px; top: 128px;
    list-style: none;
    font-size: 11px; font-weight: 400; color: var(--ink-soft);
    text-align: right;
  }
  .contact li {
    display: flex; align-items: center; justify-content: flex-end; gap: 8px;
    line-height: 17px;
  }
  .contact svg { width: 11px; height: 11px; fill: var(--green-deep); flex: none; }
  .person {
    position: absolute; left: 28px; bottom: 16px;
    display: flex; flex-direction: column; align-items: flex-end;
    color: var(--paper);
  }
  .person-name { font-size: 19px; font-weight: 400; letter-spacing: .3px; line-height: 1.2; }
  .person-title { font-size: 12px; font-weight: 300; margin-top: 1px; line-height: 1.2; }
</style>
</head>
<body>
<main class="sheet">

  <section class="card card-front" aria-label="Card front">
    <svg class="card-art" viewBox="0 0 540 309" preserveAspectRatio="none" aria-hidden="true">
      <path d="M0 175 C70 245 170 292 250 309 L0 309 Z" fill="var(--green-deep)"/>
      <path d="M360 0 C440 8 500 25 540 48 L540 0 Z" fill="var(--green-deep)"/>
    </svg>
    <div class="brand">
      <span class="brand-dot"></span>
      <span class="brand-name">Copperline Aeroworks</span>
    </div>
  </section>

  <section class="card card-back" aria-label="Card back">
    <svg class="card-art" viewBox="0 0 540 309" preserveAspectRatio="none" aria-hidden="true">
      <path d="M0 96 C140 201 320 276 540 296 L540 309 L0 309 Z" fill="var(--green-light)"/>
      <path d="M0 104 C140 209 320 284 530 309 L0 309 Z" fill="var(--paper)"/>
      <path d="M0 110 C140 215 320 290 515 309 L0 309 Z" fill="var(--green-deep)"/>
    </svg>
    <div class="brand">
      <span class="brand-dot"></span>
      <span class="brand-name">Copperline Aeroworks</span>
    </div>
    <ul class="contact">
      <li>(555) 214-7390
        <svg viewBox="0 0 24 24"><path d="M6.6 10.8a15 15 0 0 0 6.6 6.6l2.2-2.2a1 1 0 0 1 1-.25 11.4 11.4 0 0 0 3.6.57 1 1 0 0 1 1 1V20a1 1 0 0 1-1 1A17 17 0 0 1 3 4a1 1 0 0 1 1-1h3.5a1 1 0 0 1 1 1c0 1.25.2 2.45.57 3.57a1 1 0 0 1-.25 1z"/></svg>
      </li>
      <li>(888) 555-0147
        <svg viewBox="0 0 24 24"><path d="M6 3h9l3 3v4H6zM3 11h18v9H3zm3 2v2h3v-2zm0 3v2h3v-2zm5-3v2h3v-2zm0 3v2h3v-2z"/></svg>
      </li>
      <li>copperlineaeroworks.example
        <svg viewBox="0 0 24 24"><path d="M12 2a10 10 0 1 0 0 20 10 10 0 0 0 0-20zm0 2c1 1.2 1.8 3.2 2.1 6H9.9C10.2 7.2 11 5.2 12 4zM4.1 13h3.8c.1 2 .5 3.8 1.1 5.2A8 8 0 0 1 4.1 13zm0-2A8 8 0 0 1 9 5.8C8.4 7.2 8 9 7.9 11zm5.8 2h4.2c-.3 2.8-1.1 4.8-2.1 6-1-1.2-1.8-3.2-2.1-6zm6.2 0h3.8a8 8 0 0 1-4.9 5.2c.6-1.4 1-3.2 1.1-5.2zm0-2c-.1-2-.5-3.800-1.1-5.2a8 8 0 0 1 4.9 5.2z"/></svg>
      </li>
      <li>grant.whitcombe@copperlineaeroworks.example
        <svg viewBox="0 0 24 24"><path d="M2 5h20v14H2zm2 2v.4l8 5.2 8-5.2V7zm0 2.8V17h16V9.8l-8 5.2z"/></svg>
      </li>
    </ul>
    <div class="person">
      <div class="person-name">Grant L. Whitcombe</div>
      <div class="person-title">President</div>
    </div>
  </section>

</main>
</body>
</html>
```